Business Card Design Project

- makeup artist business card

- original and creative

- Elegant design

- Feel free to come out with cool designs but stick to being elegant and attractive

- Design relates to makeup

- includes name, occupation, contact numbers, email, website

- regular size business card

- round corner card

- double sided

- on 1 side it should just have the website name in the center " browsandblush.example "

Industry/Entity Type

Business

Requirements
Must have
• Marla Voss
Makeup Artist
USA: +1 (415)872-6410
Singapore: +65 83027715
marlavoss@browsandblush.example
www.browsandblush.example
Should not have
• nothing cartoon looking.
Pictures of makeup being grab from the internet.. Examples: eyes or lips.

```html
<!DOCTYPE html>
<html lang="en">
<head>
<meta charset="utf-8">
<title>Marla Voss – Makeup Artist Business Card</title>
<link rel="stylesheet" href="https://fonts.googleapis.com/css2?family=Arimo:wght@400;700&family=Libre+Baskerville:wght@700&display=swap">
<style>
  :root {
    --backdrop: #f4e6ea;
    --plum: #8a2464;
    --plum-deep: #731a52;
    --plum-light: #a23a7b;
    --rose: #e2629f;
    --rose-soft: #f08dbb;
    --ink: #1c1c1c;
    --ink-soft: #333;
    --paper: #ffffff;
  }
  * { box-sizing: border-box; margin: 0; padding: 0; }
  html, body { width: 1200px; height: 951px; overflow: hidden; }
  body {
    background: radial-gradient(ellipse at 40% 35%, #fbf3f5 0%, var(--backdrop) 75%);
    font-family: "Arimo", Arial, sans-serif;
    position: relative;
  }
  .card {
    position: absolute;
    width: 560px;
    height: 320px;
    border-radius: 22px;
    overflow: hidden;
    box-shadow: 0 14px 30px rgba(90, 20, 60, 0.22);
  }

  /* Back side */
  .card-back {
    left: 80px;
    top: 90px;
    background: radial-gradient(ellipse at 45% 35%, var(--plum-light) 0%, var(--plum) 55%, var(--plum-deep) 100%);
    display: flex;
    align-items: center;
    justify-content: center;
  }
  .back-url {
    display: flex;
    align-items: center;
    gap: 14px;
    color: #fff;
    font-size: 25px;
    letter-spacing: 2px;
  }
  .lead-dots { display: flex; align-items: center; gap: 8px; }
  .lead-dots span { display: block; border-radius: 50%; background: #fff; }
  .lead-dots span:nth-child(1) { width: 4px; height: 4px; opacity: .6; }
  .lead-dots span:nth-child(2) { width: 5px; height: 5px; opacity: .7; }
  .lead-dots span:nth-child(3) { width: 6px; height: 6px; opacity: .8; }
  .lead-dots span:nth-child(4) { width: 7px; height: 7px; opacity: .9; }
  .lead-dots span:nth-child(5) { width: 9px; height: 9px; }
  .back-url .domain { color: #f7b9d6; }

  /* Front side */
  .card-front {
    left: 560px;
    top: 540px;
    background: linear-gradient(180deg, var(--paper) 0%, #f7f7f7 100%);
  }
  .identity { position: absolute; left: 44px; top: 40px; }
  .person-name {
    font-family: "Libre Baskerville", Georgia, serif;
    font-weight: 700;
    font-size: 23px;
    color: var(--ink);
  }
  .person-role {
    font-size: 16px;
    font-style: italic;
    color: var(--rose);
    margin-top: 3px;
  }
  .brand-name {
    position: absolute;
    right: 44px;
    top: 110px;
    display: flex;
    align-items: center;
    gap: 10px;
    color: var(--plum);
    font-size: 28px;
    font-weight: 400;
    white-space: nowrap;
  }
  .brand-dot {
    width: 12px;
    height: 12px;
    border-radius: 50%;
    background: var(--plum);
    flex: none;
  }
  .contacts {
    position: absolute;
    left: 44px;
    top: 142px;
    list-style: none;
    font-size: 16px;
    color: var(--ink-soft);
  }
  .contacts li { display: flex; align-items: center; gap: 9px; height: 21px; }
  .contacts svg { width: 14px; height: 14px; flex: none; }
  .contacts .url-domain { color: var(--rose); }
  .front-waves {
    position: absolute;
    left: 0;
    bottom: 0;
    width: 560px;
    height: 100px;
  }
</style>
</head>
<body>

  <section class="card card-back" aria-label="Business card back">
    <p class="back-url">
      <span class="lead-dots" aria-hidden="true"><span></span><span></span><span></span><span></span><span></span></span>
      <span>www.<span class="domain">browsandblush</span>.example</span>
    </p>
  </section>

  <section class="card card-front" aria-label="Business card front">
    <div class="identity">
      <h1 class="person-name">Marla Voss</h1>
      <p class="person-role">Makeup Artist</p>
    </div>

    <p class="brand-name"><span class="brand-dot" aria-hidden="true"></span>brows and blush</p>

    <ul class="contacts">
      <li>
        <svg viewBox="0 0 14 14" aria-hidden="true"><circle cx="7" cy="7" r="6" fill="none" stroke="var(--plum)" stroke-width="1.4"/><path d="M5 4.2 L6.2 4 L6.8 5.8 L6 6.4 Q6.6 7.8 7.8 8.4 L8.4 7.6 L10 8.2 L9.8 9.4 Q6 9.8 5 4.2Z" fill="var(--plum)"/></svg>
        USA: +1 (415)872-6410
      </li>
      <li>
        <svg viewBox="0 0 14 14" aria-hidden="true"><circle cx="7" cy="7" r="6" fill="none" stroke="var(--plum)" stroke-width="1.4"/><path d="M5 4.2 L6.2 4 L6.8 5.8 L6 6.4 Q6.6 7.8 7.8 8.4 L8.4 7.6 L10 8.2 L9.8 9.4 Q6 9.8 5 4.2Z" fill="var(--plum)"/></svg>
        Singapore: +65 83027715
      </li>
      <li>
        <svg viewBox="0 0 14 14" aria-hidden="true"><rect x="1.5" y="3.5" width="11" height="8" rx="1" fill="var(--plum)"/><path d="M1.8 4 L7 8 L12.2 4" fill="none" stroke="#fff" stroke-width="1"/></svg>
        marlavoss@browsandblush.example
      </li>
      <li>
        <svg viewBox="0 0 14 14" aria-hidden="true"><circle cx="7" cy="7" r="6" fill="var(--plum)"/></svg>
        <span>www.<span class="url-domain">browsandblush</span>.example</span>
      </li>
    </ul>

    <svg class="front-waves" viewBox="0 0 560 100" preserveAspectRatio="none" aria-hidden="true">
      <path d="M0 30 Q230 62 560 4 L560 100 L0 100Z" fill="var(--plum)" opacity="0.85"/>
      <path d="M0 50 Q260 76 560 24 L560 100 L0 100Z" fill="var(--rose-soft)"/>
      <path d="M0 62 Q280 88 560 48 L560 100 L0 100Z" fill="var(--rose)"/>
      <path d="M0 76 Q300 98 560 70 L560 100 L0 100Z" fill="var(--plum)"/>
    </svg>
  </section>

</body>
</html>
```